ASL Learning Website Application Pages Redesign

Introduction:
We need a redesign of the internal pages of our website, SignQuiverly.com. The current website design has been in place for many years and is not mobile friendly. We want an updated design that makes the site look cleaner, more professional, and mobile accessible. We are looking for a design that eliminates the clutter on each page, and makes the site simple and easy to use. We will be interested in your design if it is unique and creative. Don't be afraid to completely change the look of the site.

We need the designs sliced up into clean HTML files that are responsive and work well on both mobile and desktop computers. We will implement the PHP needed to make the pages functional.

About Us:
SignQuiverly is a subscription-based website for American Sign Language (ASL) video lessons. The content is for anyone who wishes to learn ASL, regardless of age. It has been designed to instruct Deaf students, parents of Deaf children, and the community-at-large. All lessons are taught by Deaf experts of ASL.

Overview:
The website before log-in does not need any changes. There are five key pages within the internal website (after log-in) that need to be redesigned; they are listed below. Note that some pages (Dictionary and Activity) have multiple sub-pages, so there are about 6-8 pages in total to design, depending on how you decide to approach this (more info in the pages’ respective instruction documents).

The new page designs should retain their existing features, and as stated before, should be mobile friendly. However, you may combine, collapse, or completely change the look of these features. Each page to redesign has a separate instruction document attachment, and screenshots of the current version of the page. Our logo has also been attached. If you want to see the website pages for yourself, you can also go to our website (SignQuiverly.com) and use a free trial to get access to the internal site.

As for design preferences, we want our site to be modern-looking and mature. We’re looking for an inviting, educational style that can attract both high school students and adults. We’re happy with the current font and color scheme, but we’re always open to ideas!

Additional Notes:
- Every page has the same header and footer. You could keep these the same, or change them, based on your discretion.
- Currently, every page also has a breadcrumb. The breadcrumb is unnecessary and you may remove it. However, the “add/remove from favorites” button on the right of the breadcrumb is necessary to keep somewhere on the page.

Pages:
Here’s a list of the five key pages we need redesigned:
- Dashboard
- Dictionary
- Lesson
- Activity
- All Lessons

Each page has its own instruction document. These are attached separately.

Just purchased a $150 for Top designers. I need to give them time to submit their designs . Can I have 7 more days?

Target Market(s)

Deaf students, parents of Deaf children, and the community-at-large interested in learning ASL

Coding

Number of Pages Required

5+ page

Font styles to use
Sans Serif

Requirements
Must have
• Responsive design - the full application experience should be available on mobile devices.
Follow the directions on the design brief.
Nice to have
• Be creative! Please play around with, or even completely change, the look of the site.

```html
<!DOCTYPE html>
<html lang="en">
<head>
<meta charset="utf-8">
<title>SignQuiverly – Dashboard</title>
<link rel="stylesheet" href="https://fonts.googleapis.com/css2?family=Open+Sans:wght@400;600;700;800&display=swap">
<style>
:root{
  --green:#3ca64b;
  --green-dark:#2e8a3c;
  --green-soft:#d6ecd2;
  --ink:#2b2b2b;
  --muted:#6d6d6d;
  --line:#dedede;
  --nav:#2f2f2f;
  --panel:#f1f1f1;
  --footer:#1f1f1f;
  --footer-bottom:#151515;
  --white:#ffffff;
}
*{box-sizing:border-box;margin:0;padding:0}
html,body{width:885px;height:1200px;overflow:hidden}
body{font-family:"Open Sans",Arial,sans-serif;color:var(--ink);background:var(--white);font-size:10px;position:relative}

/* header */
.site-header{height:40px;position:relative}
.brand{position:absolute;left:20px;top:5px;display:flex;align-items:center;gap:6px}
.brand-mark{width:12px;height:12px;background:var(--green)}
.brand-name{font-size:20px;font-weight:800;color:var(--green);letter-spacing:-.4px;line-height:1}
.brand-tag{position:absolute;left:20px;top:28px;font-size:6.5px;color:var(--muted)}
.promo{position:absolute;right:14px;top:5px;width:240px;height:30px;background:var(--green);color:var(--white);text-align:center;padding-top:4px;line-height:1.25}
.promo strong{display:block;font-size:8.5px;font-weight:700;letter-spacing:.2px}
.promo span{font-size:8px}
.promo em{font-style:normal;text-decoration:underline}

/* nav */
.main-nav{height:22px;background:var(--nav);display:flex;align-items:center;padding:0 12px;gap:20px}
.main-nav a{color:var(--white);text-decoration:none;font-size:8.5px}
.main-nav .logout{margin-left:auto;background:var(--green);padding:3px 16px;font-weight:700;font-size:8px}

/* layout */
.page{display:flex;padding:0 15px 0 20px;height:978px}
.content{width:612px;padding-top:16px}
.sidebar{width:220px;margin-left:18px;padding-top:14px}

h1{font-size:12px;font-weight:700}
.dash-head{display:flex;justify-content:space-between;align-items:baseline}
.welcome{font-size:9px;font-weight:600}
.welcome a{color:var(--green)}
.recommend{display:flex;gap:12px;margin-top:14px}
.rec-box{flex:1;border:1px solid var(--line);padding:8px 10px;height:46px}
.rec-box small{display:block;font-size:8px;color:var(--muted)}
.rec-box strong{font-size:12px;color:var(--green);font-weight:700}
.rec-box.is-active{background:var(--green-soft);border-color:var(--green-soft)}

h2{font-size:12px;font-weight:700;margin:38px 0 10px}

/* progress table */
.progress{width:100%;border-collapse:collapse;font-size:8.5px}
.progress th{background:#3a3a3a;color:var(--white);text-align:left;font-weight:600;padding:8px 8px}
.progress td{padding:8px 8px;border-bottom:1px solid var(--line);height:34px}
.progress tr.is-done td{background:var(--green-soft)}
.progress td:first-child{color:var(--green-dark);text-decoration:underline}

/* my pages */
.tiles{display:grid;grid-template-columns:repeat(4,111px);gap:14px 33px;margin:22px 0 0 58px}
.tile{height:106px;border:1px solid var(--line);display:flex;flex-direction:column;align-items:center;justify-content:center;gap:10px;font-size:9.5px;font-weight:600}
.tile svg{width:34px;height:34px;fill:none;stroke:var(--ink);stroke-width:1.6}
.tile.is-current{background:var(--green);color:var(--white);border-color:var(--green)}
.tile.is-current svg{stroke:var(--white)}

/* request form */
.request{background:var(--panel);margin-top:34px;padding:18px 20px;height:182px}
.request p{font-size:10.5px;font-weight:700;line-height:1.35;width:340px}
.field{display:flex;align-items:center;gap:8px;margin-top:10px;font-size:8.5px}
.field span{width:60px;height:14px;background:var(--white);border:1px solid var(--line)}
.request .hint{font-size:9px;font-weight:600;width:auto;margin-top:14px}
.textarea{height:26px;background:var(--white);border:1px solid var(--line);margin-top:6px}
.btn{display:inline-block;margin-top:10px;background:var(--green);color:var(--white);font-weight:700;font-size:8.5px;padding:6px 14px}

/* sidebar */
.sidebar h3{font-size:11px;font-weight:700;margin-bottom:8px}
.lesson-card{margin-bottom:14px}
.lesson-card .thumb{height:118px}
.lesson-card span{display:block;font-size:9px;font-weight:600;margin-top:3px}
.t1{background:linear-gradient(135deg,#f2b53b,#e24a6a 55%,#3d8fd8)}
.t2{background:linear-gradient(135deg,#6b4b3a,#c9a37a)}
.t3{background:linear-gradient(135deg,#c84a4a,#e6c6a8)}
.t4{background:linear-gradient(135deg,#8a5a8c,#3e3e6e)}
.t5{background:linear-gradient(135deg,#3f6fa6,#d9a585)}
.t6{background:linear-gradient(135deg,#f07c3a,#e8327a 50%,#4bb6c9)}

/* footer */
.site-footer{background:var(--footer);color:#cfcfcf;height:135px;display:flex;padding:16px 22px 0;gap:30px;font-size:7.5px;line-height:1.5}
.site-footer h4{color:var(--green);font-size:10.5px;font-weight:700;margin-bottom:6px}
.foot-brand{width:130px;display:flex;align-items:center;gap:6px;align-self:flex-start;margin-top:4px}
.foot-brand .brand-mark{width:12px;height:12px}
.foot-brand b{color:var(--white);font-size:15px;font-weight:800}
.foot-about{width:190px}
.foot-links{width:210px}
.foot-links ul{list-style:none;columns:2}
.foot-contact li{list-style:none;display:flex;gap:6px;align-items:flex-start;margin-bottom:5px}
.foot-contact svg{width:10px;height:10px;fill:var(--green);flex:none;margin-top:1px}
.copyright{background:var(--footer-bottom);color:#9a9a9a;height:25px;display:flex;align-items:center;justify-content:space-between;padding:0 22px;font-size:7.5px}
.social{display:flex;gap:8px}
.social i{width:9px;height:9px;border-radius:50%;background:var(--green);display:block}
</style>
</head>
<body>

<header class="site-header">
  <div class="brand"><span class="brand-mark"></span><span class="brand-name">SignQuiverly</span></div>
  <div class="brand-tag">American Sign Language Video Lessons</div>
  <div class="promo">
    <strong>LEARN ASL THROUGH VIDEO LESSONS ONLINE</strong>
    <span>You are currently logged in as <em>marlowe.lena</em></span>
  </div>
</header>

<nav class="main-nav">
  <a href="#">Dictionary</a><a href="#">My Vocabulary</a><a href="#">Favorites</a><a href="#">Tips &amp; Grammar</a><a href="#">Multiple Meanings</a><a href="#">Lesson List</a><a href="#">Lessons</a><a href="#">Teacher Resources</a>
  <a href="#" class="logout">LOG OUT</a>
</nav>

<div class="page">
  <main class="content">
    <div class="dash-head">
      <h1>DASHBOARD</h1>
      <div class="welcome">Welcome <a href="#">marlowe.lena</a></div>
    </div>
    <div class="recommend">
      <div class="rec-box"><small>Recommended next lesson</small><strong>Colors</strong></div>
      <div class="rec-box is-active"><small>Recommended next activity</small><strong>Choose the correct sentence</strong></div>
    </div>

    <h2>Your Progress</h2>
    <table class="progress">
      <thead><tr><th>Date</th><th>Lesson</th><th>Activity</th><th>Score</th><th>Attempts</th><th>Notes</th></tr></thead>
      <tbody>
        <tr><td>10/25/2021</td><td>Colors</td><td>Match the vocabulary</td><td>100%</td><td>1</td><td>Review lesson video activity</td></tr>
        <tr class="is-done"><td>10/24/2021</td><td>Numbers 1-10</td><td>Sentence instruction</td><td>100%</td><td>1</td><td>Review lesson video activity</td></tr>
        <tr><td>10/22/2021</td><td>Numbers 1-10</td><td>Do these videos match?</td><td>100%</td><td>1</td><td>Review lesson video activity</td></tr>
        <tr class="is-done"><td>10/20/2021</td><td>Meet &amp; Greet</td><td>Choose the correct sentence</td><td>100%</td><td>1</td><td>Review lesson video activity</td></tr>
        <tr><td>10/19/2021</td><td>Meet &amp; Greet</td><td>English to ASL Practice</td><td>100%</td><td>1</td><td>Review lesson video activity</td></tr>
      </tbody>
    </table>

    <h2>My Pages</h2>
    <div class="tiles">
      <div class="tile"><svg viewBox="0 0 34 34"><path d="M5 6h10a3 3 0 0 1 2 1v22a3 3 0 0 0-2-1H5zM29 6H19a3 3 0 0 0-2 1v22a3 3 0 0 1 2-1h10z"/></svg>Dictionary</div>
      <div class="tile"><svg viewBox="0 0 34 34"><rect x="7" y="4" width="20" height="26"/><path d="M11 11h12M11 16h12M11 21h8"/></svg>My Vocabulary</div>
      <div class="tile"><svg viewBox="0 0 34 34"><path d="M17 4l4 8.5 9 1.2-6.6 6.2 1.7 9L17 24.6 8.9 29l1.7-9L4 13.7l9-1.2z"/></svg>Favorites</div>
      <div class="tile"><svg viewBox="0 0 34 34"><path d="M12 22a9 9 0 1 1 10 0v4H12zM13 30h8"/></svg>Tips And Grammar</div>
      <div class="tile"><svg viewBox="0 0 34 34"><rect x="5" y="5" width="10" height="10"/><rect x="19" y="5" width="10" height="10"/><rect x="5" y="19" width="10" height="10"/><rect x="19" y="19" width="10" height="10"/></svg>Multiple Meanings</div>
      <div class="tile"><svg viewBox="0 0 34 34"><path d="M12 9h17M12 17h17M12 25h17"/><circle cx="6" cy="9" r="1.5"/><circle cx="6" cy="17" r="1.5"/><circle cx="6" cy="25" r="1.5"/></svg>Lesson List</div>
      <div class="tile is-current"><svg viewBox="0 0 34 34"><rect x="4" y="7" width="26" height="20" rx="2"/><path d="M14 12v10l8-5z"/></svg>My Lessons</div>
    </div>

    <section class="request">
      <p>Can't find the word you're looking for? Use the form below to request that we add it to our dictionary.</p>
      <div class="field">Word to add <span></span></div>
      <p class="hint">Sample sentence or definition of the word to give us context so we can properly sign your word</p>
      <div class="textarea"></div>
      <span class="btn">SUBMIT WORD</span>
    </section>
  </main>

  <aside class="sidebar">
    <h3>Lessons</h3>
    <div class="lesson-card"><div class="thumb t1" role="img" aria-label="Lesson cover: colourful paint for the Colors lesson"></div><span>Colors</span></div>
    <div class="lesson-card"><div class="thumb t2" role="img" aria-label="Lesson cover: survival words signs"></div><span>Survival Words</span></div>
    <div class="lesson-card"><div class="thumb t3" role="img" aria-label="Lesson cover: Deaf culture"></div><span>Deaf Culture I</span></div>
    <div class="lesson-card"><div class="thumb t4" role="img" aria-label="Lesson cover: fingerspelling hands"></div><span>Fingerspelling I</span></div>
    <div class="lesson-card"><div class="thumb t5" role="img" aria-label="Lesson cover: greetings in sign language"></div><span>Meet &amp; Greet</span></div>
    <div class="lesson-card"><div class="thumb t6" role="img" aria-label="Lesson cover: bright coloured objects"></div><span>Colors II</span></div>
  </aside>
</div>

<footer class="site-footer">
  <div class="foot-brand"><span class="brand-mark"></span><b>SignQuiverly</b></div>
  <div class="foot-about">
    <h4>About Us</h4>
    <p>SignQuiverly is a subscription-based website for American Sign Language (ASL) video lessons. The content is for anyone who wishes to learn ASL, regardless of age. It has been designed to instruct Deaf students, parents of Deaf children, and the community-at-large. All lessons are taught by Deaf experts of ASL.</p>
  </div>
  <div class="foot-links">
    <h4>Quick Links</h4>
    <ul><li>Home</li><li>Try It Free</li><li>Contact Us</li><li>Group Rate Form</li><li>Teacher's Guide</li><li>Gift Certificates</li><li>FAQs</li><li>Privacy Policy</li></ul>
  </div>
  <div class="foot-contact">
    <h4>Contact Info</h4>
    <ul>
      <li><svg viewBox="0 0 10 10"><path d="M2 0l2 2.5-1 1.2a6 6 0 0 0 3.3 3.3l1.2-1L10 8l-1.4 2C4 10 0 6 0 1.4z"/></svg>(555) 014-2286</li>
      <li><svg viewBox="0 0 10 10"><path d="M5 0a3.5 3.5 0 0 1 3.5 3.5C8.5 6 5 10 5 10S1.5 6 1.5 3.5A3.5 3.5 0 0 1 5 0z"/></svg>1200 Maple Crest Ave<br>Fairview Hills, MI 00000</li>
      <li><svg viewBox="0 0 10 10"><path d="M0 2h10v6H0zM0 2l5 3.5L10 2" stroke="#1f1f1f" stroke-width=".6"/></svg>info@signquiverly.com</li>
    </ul>
  </div>
</footer>
<div class="copyright">
  <span>Copyright © 2021 SignQuiverly. All Rights Reserved.</span>
  <div class="social"><i></i><i></i><i></i></div>
</div>

</body>
</html>
```